Engineering group involved with fire safety needs a business card

We need a business card design for a company based in Greece called "Varotis Group". We are engineers and specialized technicians, operating the following : a) Fire fighting equipment trade b) Installation , Inspection & Maintenance of fire extinguishers and fire protection systems c) Occupational Health & Safety (Risk assessment & management/ Staff training). We need a clear and simple card design. I uploaded a draft I made, in order to give you an idea of the company and how I currently imagine the design of the card. I also uploaded the logo in .png file format. We are always open to different, new suggestions and ideas you may want to submit.
Target Market(s)
industries, companies, managers, retail clients
Industry/Entity Type
Fire Safety
Contact Information for Business Card
Addresses & phone numbers (headquarters + branch), logo, name (you can find all the details on the uploaded files!)
Colors
Designer to choose colors to be used in the design.
Look and feel
Each slider illustrates characteristics of the customer's brand and the style your logo design should communicate.

```html
<!DOCTYPE html>
<html lang="en">
<head>
<meta charset="utf-8">
<title>Varotis Group – Business Card</title>
<link rel="stylesheet" href="https://fonts.googleapis.com/css2?family=Montserrat:wght@400;500;600;700;800&display=swap">
<style>
  :root {
    --backdrop: #2b2c2e;
    --card-grey: #5d6163;
    --card-white: #ffffff;
    --brand-red: #b01e23;
    --text-light: #ffffff;
    --text-soft: #e3e5e6;
  }
  * { box-sizing: border-box; margin: 0; padding: 0; }
  html, body { width: 1200px; height: 900px; overflow: hidden; }
  body {
    background: radial-gradient(ellipse at 55% 40%, #45474a 0%, var(--backdrop) 75%);
    font-family: "Montserrat", sans-serif;
    color: var(--text-light);
  }
  .canvas { position: relative; width: 1200px; height: 900px; }
  .card {
    position: absolute;
    top: 135px;
    width: 360px;
    height: 630px;
    background: var(--card-grey);
    overflow: hidden;
    box-shadow: 0 18px 40px rgba(0,0,0,.45);
    text-align: center;
  }
  .card--front { left: 190px; }
  .card--back { left: 650px; }

  /* front */
  .front-top {
    height: 200px;
    background: var(--card-white);
    border-bottom: 3px solid var(--brand-red);
    display: flex; align-items: center; justify-content: center;
  }
  .brand-square { width: 70px; height: 70px; background: var(--brand-red); }
  .brand-square--outline { background: none; border: 6px solid var(--text-light); width: 64px; height: 64px; margin: 0 auto 22px; }
  .brand-name {
    font-weight: 800; font-size: 34px; letter-spacing: 1px; line-height: 1.05;
    text-transform: uppercase;
  }
  .tagline {
    display: flex; align-items: center; justify-content: center; gap: 8px;
    font-size: 10px; font-weight: 500; color: var(--text-soft); margin-top: 8px;
  }
  .tagline::before, .tagline::after { content: ""; width: 34px; height: 1.5px; background: var(--text-light); }
  .front-body { padding-top: 34px; }
  .person { margin-top: 30px; }
  .person-name { font-weight: 700; font-size: 17px; letter-spacing: .5px; text-transform: uppercase; }
  .person-role { font-size: 14px; font-weight: 500; line-height: 1.35; margin-top: 2px; }
  .icon-row { display: flex; justify-content: center; gap: 10px; margin: 14px 0 10px; }
  .icon-row svg { width: 13px; height: 13px; fill: none; stroke: var(--text-light); stroke-width: 1.6; }
  .contact-lines { font-size: 13px; line-height: 1.55; font-weight: 500; }
  .offices { margin-top: 18px; font-size: 13px; line-height: 1.5; font-weight: 500; }
  .office-label { font-weight: 700; }

  /* back */
  .back-body { padding-top: 150px; }
  .back-body .brand-name { font-size: 40px; }
  .services {
    list-style: none; margin-top: 70px;
    font-size: 14px; font-weight: 600; line-height: 1.7; text-transform: uppercase; letter-spacing: .3px;
  }
  .web { margin-top: 22px; font-size: 14px; font-weight: 600; line-height: 1.6; }
</style>
</head>
<body>
<main class="canvas">

  <section class="card card--front" aria-label="Business card front">
    <div class="front-top"><div class="brand-square"></div></div>
    <div class="front-body">
      <h1 class="brand-name">Varotis Group</h1>
      <p class="tagline">installation | inspection | maintenance</p>
      <div class="person">
        <p class="person-name">Dimitris Alexiou</p>
        <p class="person-role">Mechanical Engineer<br>OHS Consultant</p>
      </div>
      <div class="icon-row">
        <svg viewBox="0 0 16 16" aria-label="phone"><path d="M3 2h3l1 3-2 1a8 8 0 0 0 5 5l1-2 3 1v3a1 1 0 0 1-1 1A12 12 0 0 1 2 3a1 1 0 0 1 1-1z"/></svg>
        <svg viewBox="0 0 16 16" aria-label="mobile"><rect x="4" y="1" width="8" height="14" rx="1.5"/></svg>
        <svg viewBox="0 0 16 16" aria-label="email"><rect x="1.5" y="3.5" width="13" height="9"/><path d="M1.5 3.5l6.5 5 6.5-5"/></svg>
        <svg viewBox="0 0 16 16" aria-label="website"><circle cx="8" cy="8" r="6.5"/><path d="M1.5 8h13M8 1.5c-3 3.5-3 9.5 0 13M8 1.5c3 3.5 3 9.5 0 13"/></svg>
      </div>
      <p class="contact-lines">
        +30 22940 31580<br>
        +30 210 7154920 | +30 694 215 30 48<br>
        info@varotisgroup.gr | www.varotisgroup.gr
      </p>
      <p class="offices">
        <span class="office-label">Headquarters:</span><br>
        14 Aigaiou Street, 19500 Lavrio<br>
        <span class="office-label">Branch Office:</span><br>
        22 Olympou Avenue, 15124 Marousi
      </p>
    </div>
  </section>

  <section class="card card--back" aria-label="Business card back">
    <div class="back-body">
      <div class="brand-square brand-square--outline"></div>
      <h2 class="brand-name">Varotis Group</h2>
      <p class="tagline">installation | inspection | maintenance</p>
      <ul class="services">
        <li>Fire Fighting Equipment</li>
        <li>Licencing &amp; Business Registration</li>
        <li>Occupational Health &amp; Safety</li>
        <li>Staff Training</li>
      </ul>
      <p class="web">www.varotisgroup.gr info@varotisgroup.gr</p>
    </div>
  </section>

</main>
</body>
</html>
```